Brindle Works PPT design

We are looking for a fresh and funky PPT design that is both eye-catching and allows room/whitespace for us to get the content across. We are a social media agency based in China and our logo although simple sort of reflects the nature of the company. There are two main tasks for this PPT, one as a business card to show-case our case-studies, but also as a back-drop to our pitch presentations and other client presentations. These presentations are a mix of visuals, text and graphs. The key message we want to get across is that we are professional, creative and fresh. We think that using our four support colours may work but are open to suggestions.
Current website www.brindleworks-demo.com
Reason: Hi All,
as we have just guaranteed the payment we extended the deadline to allow for more submissions. Please bear with us.
Thanks,
Brindle Works Team
Reason: To see more designs, we extend the deadline to March 18, 2014. Thanks.
Target Market(s)
Marketing CMO's, company CEO's, product managers, social media managers
Industry/Entity Type
Business
Look and feel

```html
<!DOCTYPE html>
<html lang="en">
<head>
<meta charset="utf-8">
<title>Brindle Works – Content</title>
<link rel="stylesheet" href="https://fonts.googleapis.com/css2?family=Michroma&display=swap">
<style>
  :root {
    --green: #8dc63f;
    --purple: #662d91;
    --magenta: #ec008c;
    --orange: #f15a29;
    --rule: #b3b3b3;
    --ink: #1a1a1a;
    --paper: #ffffff;
  }
  * { margin: 0; padding: 0; box-sizing: border-box; }
  html, body { width: 1200px; height: 900px; overflow: hidden; background: var(--paper); }
  .slide {
    position: relative;
    width: 1200px;
    height: 900px;
    background: var(--paper);
    font-family: "Michroma", sans-serif;
    color: var(--ink);
    overflow: hidden;
  }
  .side-panel {
    position: absolute;
    left: 0; top: 0;
    width: 478px; height: 900px;
    background: var(--green);
  }
  .side-divider {
    position: absolute;
    left: 478px; top: 0;
    width: 7px; height: 900px;
    background: var(--rule);
  }
  .section-title {
    position: absolute;
    left: 27px; top: 66px;
    width: 285px;
    font-size: 30px;
    letter-spacing: 6px;
    color: var(--ink);
    font-weight: 400;
    padding-bottom: 10px;
    border-bottom: 2px solid var(--paper);
  }
  .brand {
    position: absolute;
    right: 0; top: 0;
    width: 192px;
    height: 94px;
    border-bottom: 2px solid #cfcfcf;
    display: flex;
    align-items: center;
    justify-content: flex-end;
    padding-right: 14px;
  }
  .brand-name {
    font-size: 17px;
    color: var(--ink);
    white-space: nowrap;
  }
  .chapter-list {
    position: absolute;
    left: 452px; top: 154px;
    list-style: none;
  }
  .chapter {
    display: flex;
    align-items: center;
    height: 85.5px;
  }
  .chapter-num {
    width: 54px; height: 54px;
    border: 3px solid var(--paper);
    border-radius: 6px;
    color: var(--paper);
    font-size: 25px;
    display: flex;
    align-items: center;
    justify-content: center;
    flex-shrink: 0;
  }
  .chapter-num.green { background: var(--green); }
  .chapter-num.purple { background: var(--purple); }
  .chapter-num.magenta { background: var(--magenta); }
  .chapter-num.orange { background: var(--orange); }
  .chapter-title {
    margin-left: 19px;
    font-size: 22px;
    letter-spacing: 1px;
    white-space: nowrap;
  }
  .page-marker {
    position: absolute;
    right: 0; top: 835px;
    display: flex;
    align-items: stretch;
    height: 45px;
  }
  .page-stripes { width: 40px; height: 45px; margin-right: 12px; }
  .page-number {
    width: 68px;
    background: var(--ink);
    color: var(--paper);
    font-size: 26px;
    display: flex;
    align-items: center;
    justify-content: center;
  }
</style>
</head>
<body>
<main class="slide">
  <div class="side-panel"></div>
  <div class="side-divider"></div>
  <h1 class="section-title">CONTENT</h1>

  <div class="brand"><span class="brand-name">Brindle Works</span></div>

  <ol class="chapter-list">
    <li class="chapter"><span class="chapter-num green">1</span><span class="chapter-title">CHAPTER NO. 1</span></li>
    <li class="chapter"><span class="chapter-num green">2</span><span class="chapter-title">CHAPTER NO. 2</span></li>
    <li class="chapter"><span class="chapter-num purple">3</span><span class="chapter-title">CHAPTER NO. 3</span></li>
    <li class="chapter"><span class="chapter-num purple">4</span><span class="chapter-title">CHAPTER NO. 4</span></li>
    <li class="chapter"><span class="chapter-num magenta">5</span><span class="chapter-title">CHAPTER NO. 5</span></li>
    <li class="chapter"><span class="chapter-num magenta">6</span><span class="chapter-title">CHAPTER NO. 6</span></li>
    <li class="chapter"><span class="chapter-num orange">7</span><span class="chapter-title">CHAPTER NO. 7</span></li>
    <li class="chapter"><span class="chapter-num orange">8</span><span class="chapter-title">CHAPTER NO. 8</span></li>
  </ol>

  <div class="page-marker">
    <svg class="page-stripes" viewBox="0 0 40 45" aria-hidden="true">
      <rect x="2" y="0" width="7" height="45" fill="var(--purple)"/>
      <rect x="15" y="0" width="7" height="45" fill="var(--magenta)"/>
      <rect x="28" y="0" width="7" height="45" fill="var(--orange)"/>
    </svg>
    <span class="page-number">2</span>
  </div>
</main>
</body>
</html>
```